Birchway Inspection website (same layout, different look/style)

I want to create a NEW website based off the wordpress layout of another website. I want to have the same functionality/layout but a totally different look and style. I want my new website to have the same layout and features but to look totally different (different fonts, different logo, different colors, different style).

In the files section I have included different examples of the style I am looking for. That is conservative, trusted, simple, elegant and a little boring. I am trying to have the style of an insurnace company or bank website.

Please use that kind of style but use the same wordpress layout as the target website above.

Colors: blue, grey, green

You can use the same copy, I will add that later during the project.

My company is Birchway Inspections
birchwayinspections.example
tel:
(555) 318-7624
address:
4173 Fernhollow Rd,
Sarasota, FL 34000

Target Market(s)

Inspection

Industry/Entity Type

Inspection

Number of Pages Required

3 page

Font styles to use
Sans Serif

Colors
0054AA
0677BA
7BADD7
CADEEF
E8F1F8
0094D4
00A9DD
6FCCEA
C7EBF8
E9F6FB

Requirements
Must have
• Landing page, services page, about page

```html
<!DOCTYPE html>
<html lang="en">
<head>
<meta charset="utf-8">
<title>Birchway Inspections – Get Started</title>
<link rel="stylesheet" href="https://fonts.googleapis.com/css2?family=Nunito+Sans:wght@400;600;700;800&family=Archivo:wght@500;700;800&display=swap">
<style>
:root{
  --ink:#1d2f42;
  --navy:#0054AA;
  --blue:#0677BA;
  --blue-soft:#7BADD7;
  --blue-pale:#CADEEF;
  --mist:#E8F1F8;
  --cyan:#00A9DD;
  --green:#2e9e6f;
  --line:#7b9bb8;
  --white:#ffffff;
  --sky-top:#5f93cf;
  --sky-bottom:#9cc2e8;
}
*{box-sizing:border-box;margin:0;padding:0}
html,body{width:1097px;height:1200px;overflow:hidden}
body{position:relative;font-family:"Nunito Sans",Arial,sans-serif;color:var(--ink);background:var(--white)}

/* header */
.site-header{position:absolute;left:0;top:0;width:1097px;height:95px;background:var(--white)}
.brand{position:absolute;left:104px;top:28px;display:flex;align-items:center;gap:9px}
.brand-mark{width:22px;height:22px;background:var(--green)}
.brand-name{font-family:"Archivo",Arial,sans-serif;font-weight:800;font-size:24px;color:var(--navy);letter-spacing:-.3px;line-height:1}
.cert-badge{position:absolute;left:160px;top:83px;width:70px;height:5px;background:var(--blue-pale);border-radius:3px}
.social{position:absolute;display:flex;gap:5px}
.social span{display:block;width:23px;height:23px;border-radius:50%;background:var(--navy)}
.header-social{left:659px;top:39px}
.call-pill{position:absolute;left:767px;top:31px;width:281px;height:37px;background:var(--blue-soft);
  clip-path:polygon(8% 0,100% 0,96% 60%,88% 100%,0 100%);display:flex;align-items:center;padding-left:31px;gap:8px;
  color:var(--white);font-size:14px;border-radius:0 0 22px 0}
.call-pill .icon{width:21px;height:21px;border-radius:50%;background:var(--white);display:flex;align-items:center;justify-content:center}
.call-pill b{font-weight:800}

/* nav */
.main-nav{position:absolute;left:0;top:95px;width:1097px;height:45px;background:var(--blue)}
.main-nav a{position:absolute;top:15px;color:var(--white);font-weight:800;font-size:11.5px;text-decoration:none;letter-spacing:.2px}
.nav-sep{position:absolute;top:17px;width:1px;height:11px;background:var(--blue-pale)}
.nav-cta{position:absolute;left:721px;top:0;width:376px;height:45px;background:var(--navy);clip-path:polygon(4% 0,100% 0,100% 100%,0 100%)}
.nav-cta a{left:47px;top:14px;font-size:14px;letter-spacing:.3px}

/* contact section */
.contact-section{position:absolute;left:0;top:140px;width:1097px;height:727px;
  background:linear-gradient(180deg,#f4f8fc 0%,#eef4fa 45%,#dbe7f2 75%,#e8f1f8 100%)}
.section-title{position:absolute;left:324px;top:177px;font-family:"Archivo",Arial,sans-serif;font-weight:500;font-size:37px;letter-spacing:1px;color:var(--navy)}
.title-badge{position:absolute;left:584px;top:175px;width:189px;height:48px;background:var(--blue-soft);
  clip-path:polygon(12% 0,100% 0,88% 100%,0 100%)}
.title-badge span{position:absolute;left:27px;top:4px;font-family:"Archivo",Arial,sans-serif;font-weight:800;font-size:37px;color:var(--white);letter-spacing:.5px}
.section-sub{position:absolute;left:0;width:1097px;top:236px;text-align:center;font-size:15.5px;color:var(--ink)}

.form-card{position:absolute;left:114px;top:290px;width:889px;height:502px;background:var(--white);
  border:1px solid var(--blue-pale);border-radius:56px 0 56px 0}
.field{position:absolute;left:157px;width:343px;height:43px;border:1px solid var(--line);background:var(--white);
  display:flex;align-items:center;padding-left:17px;gap:10px;font-size:14.5px;color:#4c5d6e;letter-spacing:.3px}
.field svg{flex:none}
.require-label{position:absolute;left:161px;top:547px;font-weight:700;font-size:12px;color:var(--ink)}
.check{position:absolute;display:flex;align-items:center;gap:7px;font-size:11.5px;color:#4c5d6e;letter-spacing:.2px}
.check i{display:block;width:15px;height:13px;border:1px solid var(--line)}
.message{position:absolute;left:157px;top:621px;width:343px;height:80px;border:1px solid var(--line);
  padding:12px 0 0 13px;display:flex;gap:8px;font-size:14.5px;color:#4c5d6e}
.send-btn{position:absolute;left:161px;top:711px;width:147px;height:38px;background:var(--green);border-radius:16px 0 16px 0;
  color:var(--white);font-weight:800;font-size:12px;letter-spacing:.3px;display:flex;align-items:center;justify-content:center}
.hero-photo{position:absolute;left:560px;top:302px;width:392px;height:392px;border-radius:50%;
  background:linear-gradient(180deg,var(--sky-top) 0%,var(--sky-bottom) 40%,#6d7479 60%,#3e4246 100%)}

/* footer */
.site-footer{position:absolute;left:0;top:867px;width:1097px;height:333px;background:var(--mist)}
.footer-panel{position:absolute;left:0;top:0}
.footer-brand{position:absolute;left:96px;top:70px;display:flex;align-items:center;gap:10px}
.footer-brand .brand-mark{background:var(--green);width:24px;height:24px}
.footer-brand .brand-name{color:var(--white);font-size:25px;line-height:1.05}
.footer-badge{position:absolute;left:118px;top:152px;width:70px;height:5px;background:var(--blue-soft);border-radius:3px}
.footer-social{left:144px;top:176px}
.footer-social span{background:var(--white)}
.footer-heading{position:absolute;top:71px;font-family:"Archivo",Arial,sans-serif;font-weight:700;font-size:15.5px;color:var(--navy);
  padding-left:9px;border-left:2px solid var(--green);line-height:16px}
.footer-link{position:absolute;left:403px;font-size:12.7px;color:var(--ink);letter-spacing:.3px}
.contact-row{position:absolute;left:565px;display:flex;align-items:center;gap:10px;font-size:12px;color:var(--ink)}
.contact-row .icon{width:22px;height:22px;border-radius:50%;background:var(--navy);display:flex;align-items:center;justify-content:center;flex:none}
.map{position:absolute;left:792px;top:100px;width:211px;height:141px;background:linear-gradient(135deg,#e3ebf2,#c9d7e3)}
.footer-rule{position:absolute;left:208px;top:298px;width:873px;height:1px;background:var(--blue-pale)}
.copyright{position:absolute;left:0;width:1097px;top:317px;text-align:center;font-size:11px;color:var(--ink);padding-left:30px}
.copyright u{text-underline-offset:2px}
</style>
</head>
<body>

<header class="site-header">
  <div class="brand"><span class="brand-mark"></span><span class="brand-name">Birchway Inspections</span></div>
  <div class="cert-badge"></div>
  <div class="social header-social" aria-label="Social links"><span></span><span></span><span></span></div>
  <div class="call-pill">
    <span class="icon"><svg width="11" height="11" viewBox="0 0 24 24"><path fill="#0054AA" d="M6.6 10.8a15 15 0 0 0 6.6 6.6l2.2-2.2a1 1 0 0 1 1-.25 11.4 11.4 0 0 0 3.6.57 1 1 0 0 1 1 1V20a1 1 0 0 1-1 1A17 17 0 0 1 3 4a1 1 0 0 1 1-1h3.5a1 1 0 0 1 1 1c0 1.250.2 2.450.57 3.57a1 1 0 0 1-.25 1z"/></svg></span>
    <span>CALL TODAY <b>(555) 318 7624</b></span>
  </div>
</header>

<nav class="main-nav">
  <a style="left:135px">HOME</a>
  <a style="left:221px">ABOUT US</a><span class="nav-sep" style="left:303px"></span>
  <a style="left:326px">INSPECTION SERVICES</a><span class="nav-sep" style="left:486px"></span>
  <a style="left:507px">REVIEWS</a><span class="nav-sep" style="left:585px"></span>
  <a style="left:605px">PAY ONLINE</a>
  <div class="nav-cta"><a>REQUEST INSPECTION</a></div>
</nav>

<section class="contact-section" role="img" aria-label="Faded background photo of a suburban street and shingle roof"></section>

<h1 class="section-title">GET STARTED</h1>
<div class="title-badge"><span>TODAY</span></div>
<p class="section-sub">Fill our conact form below &amp; get started today.</p>

<div class="form-card"></div>

<div class="field" style="top:338px"><svg width="11" height="14" viewBox="0 0 24 32"><path fill="#7BADD7" d="M12 0a11 11 0 0 0-11 11c0 8 11 21 11 21s11-13 11-21A11 11 0 0 0 12 0zm0 15a4 4 0 1 1 0-8 4 4 0 0 1 0 8z"/></svg>Address</div>
<div class="field" style="top:389px"><svg width="13" height="10" viewBox="0 0 26 20"><path fill="#7BADD7" d="M0 2l13 9 13-9V0H0zm0 4v14h26V6l-13 9z"/></svg>Email address</div>
<div class="field" style="top:441px"><svg width="12" height="13" viewBox="0 0 24 26"><circle cx="12" cy="7" r="6" fill="#7BADD7"/><path fill="#7BADD7" d="M0 26c0-8 5-12 12-12s12 4 12 12z"/></svg>Full Name</div>
<div class="field" style="top:491px"><svg width="12" height="12" viewBox="0 0 24 24"><path fill="#7BADD7" d="M6.6 10.8a15 15 0 0 0 6.6 6.6l2.2-2.2a1 1 0 0 1 1-.25 11.4 11.4 0 0 0 3.6.57 1 1 0 0 1 1 1V20a1 1 0 0 1-1 1A17 17 0 0 1 3 4a1 1 0 0 1 1-1h3.5a1 1 0 0 1 1 1c0 1.25.2 2.45.57 3.57a1 1 0 0 1-.25 1z"/></svg>Phone</div>

<div class="require-label">I Require:</div>
<div class="check" style="left:161px;top:572px"><i></i>Wind Mitigation</div>
<div class="check" style="left:318px;top:570px"><i></i>Roof Certification</div>
<div class="check" style="left:161px;top:595px"><i></i>4 Point Inspection</div>
<div class="check" style="left:318px;top:593px"><i></i>Other</div>

<div class="message"><svg width="13" height="11" viewBox="0 0 26 22" style="margin-top:4px"><path fill="#7BADD7" d="M13 0C6 0 0 4 0 9c0 3 2 5 4 7l-2 6 7-4c1 .3 2.6.5 4 .5 7 0 13-4 13-9S20 0 13 0z"/></svg>Message</div>
<div class="send-btn">SEND MESSAGE</div>

<div class="hero-photo" role="img" aria-label="Photo of a shingled house roof with gables against a blue sky"></div>

<footer class="site-footer">
  <svg class="footer-panel" width="377" height="333" viewBox="0 0 377 333"><polygon points="0,0 377,0 208,333 0,333" fill="#0054AA"/></svg>
  <div class="footer-brand"><span class="brand-mark"></span><span class="brand-name">Birchway<br>Inspections</span></div>
  <div class="footer-badge"></div>
  <div class="social footer-social" aria-label="Social links"><span></span><span></span><span></span></div>

  <h3 class="footer-heading" style="left:391px">QUICK LINKS</h3>
  <h3 class="footer-heading" style="left:553px">CONTACT US</h3>
  <h3 class="footer-heading" style="left:780px">LOCATION</h3>

  <div class="footer-link" style="top:105px">Request Inspection</div>
  <div class="footer-link" style="top:132px">Our Services</div>
  <div class="footer-link" style="top:159px">About Us</div>
  <div class="footer-link" style="top:186px">Contact Us</div>

  <div class="contact-row" style="top:102px"><span class="icon"><svg width="11" height="11" viewBox="0 0 24 24"><path fill="#fff" d="M6.6 10.8a15 15 0 0 0 6.6 6.6l2.2-2.2a1 1 0 0 1 1-.25 11.4 11.4 0 0 0 3.6.57 1 1 0 0 1 1 1V20a1 1 0 0 1-1 1A17 17 0 0 1 3 4a1 1 0 0 1 1-1h3.5a1 1 0 0 1 1 1c0 1.25.2 2.45.57 3.57a1 1 0 0 1-.25 1z"/></svg></span>(555) 318 7624</div>
  <div class="contact-row" style="top:132px"><span class="icon"><svg width="12" height="9" viewBox="0 0 26 20"><rect x="1" y="1" width="24" height="18" fill="none" stroke="#fff" stroke-width="2"/><path d="M1 1l12 10L25 1" fill="none" stroke="#fff" stroke-width="2"/></svg></span>hi@birchwayinspections.example</div>

  <div class="map" role="img" aria-label="Street map showing the office location"></div>

  <div class="footer-rule"></div>
  <p class="copyright">© 2024 <u>Birchway Inspections</u>. All Rights Reserved</p>
</footer>

</body>
</html>
```